Brindle cards

I am in the auto motive, transportation business I would like a business card that is Something cool, modern edgy, having to do with car culture. I offer towing service for high and exotic cars. I also provide towing for collisions and car accidents. I offer open and enclosed transport nationwide.

Target Market(s)

Car culture people high end auto collectors

Industry/Entity Type

Towing car carrier

Contact Information for Business Card

My company colors black yellow and silver

Font styles to use
Serif

```html
<!DOCTYPE html>
<html lang="en">
<head>
<meta charset="utf-8">
<title>Brindle Transportation Business Card</title>
<link href="https://fonts.googleapis.com/css2?family=Poppins:wght@400;500;700&display=swap" rel="stylesheet">
<style>
  :root {
    --backdrop: #e4e4e4;
    --card: #ffffff;
    --ink: #111111;
    --accent-red: #d9131b;
    --accent-green: #5fb32c;
    --accent-gold: #d6a51c;
    --brand-yellow: #f7dc4e;
  }
  html, body {
    margin: 0;
    padding: 0;
    width: 1200px;
    height: 900px;
    overflow: hidden;
    background: var(--backdrop);
    font-family: 'Poppins', sans-serif;
  }
  .canvas {
    position: relative;
    width: 1200px;
    height: 900px;
  }
  .card {
    position: absolute;
    top: 217px;
    width: 308px;
    height: 499px;
    background: var(--card);
    box-shadow: 1px 2px 3px rgba(0,0,0,0.35);
  }
  .card-front {
    left: 279px;
    border-top-right-radius: 66px;
    border-bottom-left-radius: 66px;
  }
  .card-back {
    left: 617px;
    border-top-left-radius: 66px;
    border-bottom-right-radius: 66px;
  }
  .brand {
    position: absolute;
    left: 0;
    right: 0;
    display: flex;
    flex-direction: column;
    align-items: center;
    font-weight: 700;
    color: var(--ink);
    text-transform: uppercase;
  }
  .brand-mark {
    background: var(--brand-yellow);
  }
  .brand-name,
  .brand-line {
    display: block;
    line-height: 1;
  }
  .card-front .brand { top: 138px; }
  .card-front .brand-mark { width: 78px; height: 78px; margin-bottom: 18px; }
  .card-front .brand-name { font-size: 56px; letter-spacing: 1px; }
  .card-front .brand-line { font-size: 21.5px; letter-spacing: 0.5px; margin-top: 10px; }
  .card-back .brand { top: 66px; }
  .card-back .brand-mark { width: 64px; height: 64px; margin-bottom: 15px; }
  .card-back .brand-name { font-size: 48px; letter-spacing: 1px; }
  .card-back .brand-line { font-size: 18.5px; letter-spacing: 0.5px; margin-top: 9px; }
  .details {
    position: absolute;
    left: 32px;
    top: 308px;
  }
  .person-name {
    margin: 0;
    font-size: 20px;
    font-weight: 500;
    line-height: 22px;
    color: var(--accent-red);
  }
  .person-role {
    margin: 0;
    font-size: 15px;
    line-height: 18px;
    color: var(--accent-green);
  }
  .contact-list {
    list-style: none;
    margin: 12px 0 0;
    padding: 0;
  }
  .contact-list li {
    display: flex;
    align-items: center;
    gap: 5px;
    font-size: 15px;
    line-height: 18px;
    color: var(--ink);
  }
  .contact-list svg {
    width: 13px;
    height: 13px;
    fill: var(--accent-gold);
    flex: none;
  }
  .address {
    margin: 14px 0 0;
    font-size: 15px;
    line-height: 18px;
    color: var(--ink);
  }
</style>
</head>
<body>
<div class="canvas">
  <section class="card card-front">
    <div class="brand">
      <span class="brand-mark"></span>
      <span class="brand-name">Brindle</span>
      <span class="brand-line">Transportation</span>
    </div>
  </section>

  <section class="card card-back">
    <div class="brand">
      <span class="brand-mark"></span>
      <span class="brand-name">Brindle</span>
      <span class="brand-line">Transportation</span>
    </div>
    <div class="details">
      <p class="person-name">MARCUS HALE</p>
      <p class="person-role">Managing Director</p>
      <ul class="contact-list">
        <li>
          <svg viewBox="0 0 24 24" aria-hidden="true"><path d="M6.6 10.8a15 15 0 0 0 6.6 6.6l2.2-2.2a1 1 0 0 1 1-.25 11.4 11.4 0 0 0 3.6.6 1 1 0 0 1 1 1V20a1 1 0 0 1-1 1A17 17 0 0 1 3 4a1 1 0 0 1 1-1h3.5a1 1 0 0 1 1 1 11.4 11.4 0 0 0 .6 3.6 1 1 0 0 1-.25 1z"/></svg>
          044-123 456 789
        </li>
        <li>
          <svg viewBox="0 0 24 24" aria-hidden="true"><path d="M2 5h20v14H2z"/><path d="M2 5l10 8 10-8v2l-10 8L2 7z" fill="#fff"/></svg>
          info@webname.com
        </li>
        <li>
          <svg viewBox="0 0 24 24" aria-hidden="true"><path d="M12 2a10 10 0 1 0 0 20 10 10 0 0 0 0-20zm0 2c.9 1.2 1.6 2.5 2 4h-4c.4-1.5 1.1-2.8 2-4zM4.3 14a8 8 0 0 1 0-4h3.4a16 16 0 0 0 0 4zm.8 2h3a14 14 0 0 0 1.4 3.6A8 8 0 0 1 5.1 16zm3-8h-3a8 8 0 0 1 4.4-3.6A14 14 0 0 0 8.1 8zM12 20c-.9-1.2-1.6-2.5-2-4h4c-.4 1.5-1.1 2.8-2 4zm2.3-6H9.7a14 14 0 0 1 0-4h4.6a14 14 0 0 1 0 4zm.2 5.6A14 14 0 0 0 15.9 16h3a8 8 0 0 1-4.4 3.6zm1.8-5.6a16 16 0 0 0 0-4h3.4a8 8 0 0 1 0 4zm-.4-6a14 14 0 0 0-1.4-3.6A8 8 0 0 1 18.9 8z"/></svg>
          www.websitename.com
        </li>
      </ul>
      <p class="address">421, Address line goes here<br>45452,Country Name</p>
    </div>
  </section>
</div>
</body>
</html>
```